Tail Haven Pet Services ABN 31 640 975 208 needs a Postcard Design

Genuine pet lover offering a professional and highly personalised pet service. I will visit your home daily to care for your pet in their own environment. THE OTHER OPTION FOR WHEN YOU GO ON HOLIDAYS. Dog Holiday Service (includes but not limited to) Feed, Water, Walk, Love & Play. Clean Litter Trays, Hutches & Cages. Administer Medication as Directed. Water Pot Plants & Collec Mail. Individual Dog Walking (Permanent or Casual). REASONABLE RATES. Police Check & References available upon request. Contact MARGOT 0412 846 293

```html
<!DOCTYPE html>
<html lang="en">
<head>
<meta charset="utf-8">
<title>Tail Haven Pet Services – Postcard</title>
<link rel="stylesheet" href="https://fonts.googleapis.com/css2?family=Questrial&family=Righteous&display=swap">
<style>
:root{
  --red:#e41e26;
  --teal:#2bbfc0;
  --teal-light:#bfe9ea;
  --teal-pale:#e4f4f4;
  --ink:#4a4a4a;
  --white:#ffffff;
  --bg:#efefef;
}
*{margin:0;padding:0;box-sizing:border-box}
html,body{width:950px;height:1200px;overflow:hidden;background:var(--bg)}
body{position:relative;font-family:"Questrial",sans-serif}
.card{position:absolute;background:var(--white);overflow:hidden;box-shadow:0 4px 14px rgba(0,0,0,.25)}
.card--front{left:85px;top:25px;width:714px;height:550px}
.card--back{left:139px;top:608px;width:710px;height:550px}
.heading{font-family:"Righteous",sans-serif;color:var(--red);font-variant:small-caps;white-space:nowrap;font-weight:400}

/* front */
.front-photo{position:absolute;inset:0;background:linear-gradient(180deg,#e9e6e0 0%,#c9b493 35%,#6d604f 60%,#d9c3b4 80%,#efe4dc 100%)}
.front-title{position:absolute;left:26px;top:32px;font-size:22px}
.front-wave{position:absolute;left:0;bottom:0;width:714px;height:140px}
.front-contact{position:absolute;left:34px;top:480px;display:flex;align-items:center;white-space:nowrap}
.front-contact svg{margin-right:10px}
.front-contact .label{color:var(--white);font-size:19px;font-variant:small-caps}
.front-contact .number{font-family:"Righteous",sans-serif;color:var(--red);font-size:27px;margin-left:12px}
.services{position:absolute;left:461px;top:283px;width:236px;height:236px;border-radius:50%;background:var(--red);box-shadow:0 0 0 5px var(--white),0 0 0 6px #cfcfcf;display:flex;flex-direction:column;align-items:center;justify-content:center;transform:rotate(-15deg);color:var(--white);text-align:center;font-variant:small-caps;line-height:1.05}
.services li{list-style:none;font-size:20px;white-space:nowrap}
.services li.mid{font-size:17px}
.services li.small{font-size:12px}

/* back */
.dogs-strip{position:absolute;left:25px;top:25px;width:390px;height:85px;background:linear-gradient(90deg,#5b5047,#d9cfc2 25%,#f1ebe2 45%,#b58850 70%,#8a4b2a 90%)}
.intro{position:absolute;left:19px;top:91px;width:395px;height:93px;border:2px solid var(--teal);background:var(--teal-pale);padding:9px 14px 0 24px;color:var(--ink);font-size:15px;line-height:17px;font-variant:small-caps}
.intro p+p{margin-top:8px}
.badge{position:absolute;left:363px;top:164px;width:60px;height:60px;border-radius:50%;background:var(--red);box-shadow:0 0 0 2px var(--white),0 0 0 3px var(--red);color:var(--white);font-family:"Righteous",sans-serif;font-size:7px;text-transform:uppercase;display:flex;align-items:center;justify-content:center;text-align:center;transform:rotate(-15deg);line-height:1.2}
.credentials{position:absolute;left:22px;top:204px;width:380px;text-align:center;color:var(--red);font-size:15px;line-height:18px;letter-spacing:.6px;font-variant:small-caps}
.back-title{position:absolute;left:19px;top:249px;font-size:19px}
.back-contact{position:absolute;left:19px;top:275px;width:390px;height:44px;border:2px solid var(--teal);display:flex;align-items:center;padding-left:24px;white-space:nowrap}
.back-contact svg{margin-right:8px}
.back-contact .label{color:var(--teal);font-size:15px;font-variant:small-caps}
.back-contact .number{font-family:"Righteous",sans-serif;color:var(--teal);font-size:23px;margin-left:12px}
.stamp{position:absolute;left:570px;top:38px;width:110px;height:106px;border:2px solid #cfcfcf}
.address-line{position:absolute;left:440px;width:230px;border-top:2px solid #d4d4d4}
.back-wave{position:absolute;left:0;bottom:0;width:710px;height:70px}
</style>
</head>
<body>

<section class="card card--front">
  <div class="front-photo" role="img" aria-label="Photo of three small black dogs resting on a beige sofa"></div>
  <h1 class="front-title heading">Tail Haven Pet Services ABN 31 640 975 208</h1>
  <svg class="front-wave" viewBox="0 0 714 140" preserveAspectRatio="none" aria-hidden="true">
    <path d="M0 40 C200 5 420 20 714 45 L714 140 L0 140 Z" fill="var(--teal-light)"/>
    <path d="M0 55 C220 25 430 40 714 70 L714 140 L0 140 Z" fill="var(--teal)"/>
    <path d="M0 118 C250 105 480 112 714 125 L714 140 L0 140 Z" fill="#5ccfd0" opacity=".6"/>
  </svg>
  <div class="front-contact">
    <svg width="42" height="34" viewBox="0 0 42 34" aria-hidden="true">
      <path d="M2 12 C4 3 38 3 40 12 L40 16 L30 16 L30 11 L12 11 L12 16 L2 16 Z" fill="var(--red)"/>
      <path d="M8 18 L34 18 L39 33 L3 33 Z" fill="var(--red)"/>
      <circle cx="21" cy="25" r="5.5" fill="var(--white)"/>
      <circle cx="21" cy="25" r="2.5" fill="var(--red)"/>
    </svg>
    <span class="label">Contact MARGOT</span>
    <span class="number">0412 846 293</span>
  </div>
  <ul class="services">
    <li>Feed</li>
    <li>Water • Walk</li>
    <li>Love &amp; Play</li>
    <li>Clean Litter Trays</li>
    <li>Hutches &amp; Cages</li>
    <li class="small">Administer Medication as Directed</li>
    <li class="mid">Individual Dog Walking</li>
    <li class="small">(Permanent or Casual)</li>
    <li class="mid">Water Pot Plants &amp;</li>
    <li class="mid">Collec Mail</li>
  </ul>
</section>

<section class="card card--back">
  <div class="dogs-strip" role="img" aria-label="Row of five dogs of different breeds peeking over the text panel"></div>
  <div class="intro">
    <p>Genuine pet lover offering a professional and highly personalised pet service.</p>
    <p>I will visit your home daily to care for your pet in their own environment.</p>
  </div>
  <div class="badge">Reasonable<br>rates!</div>
  <p class="credentials">Police Check &amp; References<br>available upon request!</p>
  <h2 class="back-title heading">Tail Haven Pet Services ABN 31 640 975 208</h2>
  <div class="back-contact">
    <svg width="38" height="30" viewBox="0 0 42 34" aria-hidden="true">
      <path d="M2 12 C4 3 38 3 40 12 L40 16 L30 16 L30 11 L12 11 L12 16 L2 16 Z" fill="var(--teal)"/>
      <path d="M8 18 L34 18 L39 33 L3 33 Z" fill="var(--teal)"/>
      <circle cx="21" cy="25" r="5.5" fill="var(--white)"/>
      <circle cx="21" cy="25" r="2.5" fill="var(--teal)"/>
    </svg>
    <span class="label">Contact MARGOT</span>
    <span class="number">0412 846 293</span>
  </div>
  <div class="stamp"></div>
  <div class="address-line" style="top:268px"></div>
  <div class="address-line" style="top:303px"></div>
  <div class="address-line" style="top:338px"></div>
  <svg class="back-wave" viewBox="0 0 710 70" preserveAspectRatio="none" aria-hidden="true">
    <path d="M0 10 C200 0 450 5 710 12 L710 70 L0 70 Z" fill="var(--teal-light)"/>
    <path d="M0 18 C220 10 470 20 710 30 L710 70 L0 70 Z" fill="var(--teal)"/>
  </svg>
</section>

</body>
</html>
```